Business Card Design

I need a business card design. I am a sole practitioner.I am a psychotherapist and I need a professional card. I am also an art therapist (a form of psychotherapy using art) so I want the image to be professional/creative/maybe ethnic. I do not want a boring minimalist "medical" image, nor do I want it too hippy/tree hugging.
Colours like reds/ochres/yellows would be good.
Industry/Entity Type
Business
Contact Information for Business Card
Mira Tanvel
Psychotherapy, Counselling and Art Therapy
Korrabel Lodge Counselling and Wellbeing services
17 Farrow Lane, Pelbury 4091
0419362750 www.MiraTanvel.com.au
on rear of card I need the option to have at least 4 or 5 appointment times /dates
Look and feel
Each slider illustrates characteristics of the customer's brand and the style your logo design should communicate.

```html
<!DOCTYPE html>
<html lang="en">
<head>
<meta charset="utf-8">
<title>Mira Tanvel Psychotherapy – Business Card</title>
<link rel="stylesheet" href="https://fonts.googleapis.com/css2?family=Oswald:wght@500&family=Open+Sans:wght@400;600&display=swap">
<style>
  :root {
    --page-bg: #ece7e0;
    --card-white: #ffffff;
    --band: #9a4a2e;
    --ink: #5e5650;
    --ochre: #c98b2b;
    --on-band: #ffffff;
    --rule: #d9cfc4;
  }
  * { box-sizing: border-box; margin: 0; padding: 0; }
  html, body {
    width: 1200px; height: 1013px; overflow: hidden;
    background: var(--page-bg);
    font-family: "Open Sans", Arial, sans-serif;
  }
  .canvas { position: relative; width: 1200px; height: 1013px; }
  .card {
    position: absolute; left: 220px; width: 760px; height: 434px;
    background: var(--card-white);
    box-shadow: 0 6px 18px rgba(0,0,0,0.14);
    overflow: hidden;
  }
  .card--front { top: 48px; }
  .card--back { top: 531px; }

  .brand { display: flex; align-items: center; gap: 14px; white-space: nowrap; }
  .brand__dot { width: 46px; height: 46px; border-radius: 50%; background: var(--ochre); flex: none; }
  .brand__name { font-weight: 600; color: var(--ink); font-size: 25px; line-height: 1.2; }
  .brand__tagline { color: var(--ochre); font-size: 17px; line-height: 1.3; }
  .card--front .brand { position: absolute; left: 48px; top: 52px; }

  .contact-band {
    position: absolute; left: 0; right: 0; top: 168px; bottom: 0;
    background: var(--band); color: var(--on-band);
  }
  .person { position: absolute; left: 48px; top: 48px; }
  .person__name {
    font-family: "Oswald", "Arial Narrow", sans-serif; font-weight: 500;
    font-size: 38px; letter-spacing: 0.5px; line-height: 1.1;
  }
  .person__role { font-size: 13px; letter-spacing: 1.5px; margin-top: 6px; }
  .address { position: absolute; left: 48px; bottom: 42px; font-size: 15px; line-height: 1.8; letter-spacing: 0.5px; }

  .contact-list { position: absolute; right: 48px; top: 36px; list-style: none; }
  .contact-list li { display: flex; align-items: center; gap: 10px; font-size: 14px; line-height: 1; margin-bottom: 14px; letter-spacing: 0.6px; }
  .contact-list svg { width: 16px; height: 16px; flex: none; fill: none; stroke: var(--on-band); stroke-width: 1.8; }

  .card--back .brand { position: absolute; left: 50%; top: 34px; transform: translateX(-50%); }
  .card--back .brand__name { font-size: 24px; }
  .card--back .brand__dot { width: 42px; height: 42px; }

  .appointments { position: absolute; left: 60px; right: 60px; top: 128px; }
  .appointments__title {
    font-family: "Oswald", "Arial Narrow", sans-serif; font-weight: 500;
    font-size: 18px; letter-spacing: 2px; color: var(--band);
    border-bottom: 3px solid var(--ochre); padding-bottom: 6px; margin-bottom: 6px;
  }
  .slot { display: flex; gap: 28px; height: 48px; align-items: flex-end; padding-bottom: 6px; border-bottom: 1px solid var(--rule); font-size: 14px; color: var(--ink); }
  .slot span { flex: 1; }
</style>
</head>
<body>
<main class="canvas">
  <section class="card card--front" aria-label="Card front">
    <div class="brand">
      <span class="brand__dot"></span>
      <div>
        <p class="brand__name">Mira Tanvel Psychotherapy</p>
        <p class="brand__tagline">Counselling and Art Therapy</p>
      </div>
    </div>
    <div class="contact-band">
      <div class="person">
        <p class="person__name">MIRA TANVEL</p>
        <p class="person__role">PSYCHOTHERAPIST &amp; ART THERAPIST</p>
      </div>
      <ul class="contact-list">
        <li><svg viewBox="0 0 16 16"><path d="M3 1.5l3 .5 1 3-1.8 1.4a8 8 0 0 0 4.4 4.4L11 9l3 1 .5 3-1.8 1.5C7 14 2 9 1.5 3.3z"/></svg>0419 362 750</li>
        <li><svg viewBox="0 0 16 16"><rect x="4" y="1" width="8" height="14" rx="1.5"/><path d="M7 12.5h2"/></svg>0427 815 093</li>
        <li><svg viewBox="0 0 16 16"><rect x="2" y="6" width="12" height="8" rx="1"/><path d="M5 6V2h6v4M5 10h6"/></svg>07 3186 4402</li>
        <li><svg viewBox="0 0 16 16"><rect x="1.5" y="3.5" width="13" height="9" rx="1"/><path d="M1.5 4l6.5 5 6.5-5"/></svg>hello@miratanvel.com.au</li>
        <li><svg viewBox="0 0 16 16"><circle cx="8" cy="8" r="6.5"/><path d="M1.5 8h13M8 1.5c-3 3.5-3 9.5 0 13M8 1.5c3 3.5 3 9.5 0 13"/></svg>www.MiraTanvel.com.au</li>
      </ul>
      <p class="address">17 Farrow Lane,<br>Pelbury 4091</p>
    </div>
  </section>

  <section class="card card--back" aria-label="Card back">
    <div class="brand">
      <span class="brand__dot"></span>
      <div>
        <p class="brand__name">Mira Tanvel Psychotherapy</p>
        <p class="brand__tagline">Counselling and Art Therapy</p>
      </div>
    </div>
    <div class="appointments">
      <p class="appointments__title">YOUR APPOINTMENTS</p>
      <div class="slot"><span>Date:</span><span>Time:</span></div>
      <div class="slot"><span>Date:</span><span>Time:</span></div>
      <div class="slot"><span>Date:</span><span>Time:</span></div>
      <div class="slot"><span>Date:</span><span>Time:</span></div>
      <div class="slot"><span>Date:</span><span>Time:</span></div>
    </div>
  </section>
</main>
</body>
</html>
```